Coaching landingpage/salespage need a layout

Hi!
We are two people from Sweden looking for help to design our coaching landingpage/salespage.

What about:
We need a nice modern timeless appealing Photoshop layout (landingpage) for our coaching page where we coach people to “how to get a richer lifestyle”.

Style of page:
We want the site to reflect seriousness but still harmonic. We would like somewhat colorful and (but not too crazy). After all, we are coaching about investments and private economy.
Responsive layout – consider stacking order when scaling down window width. Fullpage-design where content areas are 960 grid/max-width.

----------------------------------------------------------------------------
Content on page:
*Headersection – Logo and header image with the two coaches together and space for later on adding a video.

*On the landingpage the customers can read up on what we mean by a richer lifestyle (use dummy text). We show our Vardagskartan (= Lifestyle matrix) and a little description about that. If the customers want to know more, they can click "read more (or a symbolic icon that relates to read more)" to expand a hidden div (section) where they can read more about Vardagskartan. They can also minimize the section.

*3-4 Unique selling points “Four reasons why choose coaching” with nice designed number-icons and some place for text.

*The customer should also be able to read something about what happens during a typical coaching session, some bullets that summarize it (use dummy text) and a couple of headlines, maybe 3 or 4 (about what they need to prepare for themselves .eg Skype, headset/microphone etc).

*Offer/product section: A section where the customer can see what services we provide, choose product and click order. When customer click order they will arrive to an order-page (this one you don’t have to design) .
Our products are as followed: Bronze (single coaching session), Silver (small-package), Gold (large-package). Use provided graphics for these products.

*Testimonials section. Currently we have 2 good testimonials, but only with text no portrait picture.

Testimonial1: “Uppiggande och inspirerande! Kommer med enkla vardagstips såväl som svårare tips. Ett roligt sätt att få en spark i baken, så att ekonomi-energin bibehålls! Tack för ett bra samtal!" - Annelie Brunstedt

Testimonial2: "Värdefullast för mig var kunskapen om alternativa investeringssställen som inte är börs eller eget ägande." - Josefin Harkeby

*Section with portraits and info about the coaches (currently 2 coaches, but in future will be several, so a design-section that’s lets us add more coaches).

*Footer-section
------------------------------------------------------------------------

Colors:
Use Vardagskartan (attached file) as colorinspiration. Doesn’t have to be exactly those colors, you can use similar colors if it is more pleasing to the eye and you can also use complementary colors.

Currently we have tried of our own but don't really nail it with any apealing design. This is what we have done so far but we want to replace it with your more professional design:

https://www.kelbrostudio.se/full/Page/coaching13
-------------------------------------------------------------

SUMMARIZE of the above design-description:

* Our logo (attached psd-file with smart-object. You can try different colors with color-overlay)

*Apealing headerimage with portrait (attached file "big_portrait")

*Introduction text (use dummy text about 100 words)

*Text about Vardagskartan (use dummy text about 200 words)

*Vardagskartan (attached psd-file with smart-object)

*What we are covering during a coaching session (dummy text about 200 words and about 5 or 6 bullets)

*3-4 Unique Selling Points with stylish number icons (not 2 small) and some text.
*Our offers Bronze, Silver, Gold (attached pictures)
*Testimonials
*Picture & info about coaches (attached pictures, choose whichever suits you)
*Footer

Please comment if there are questions.

Reagards Henrik @ Kelbro Studio

Target Market(s)

People who want to learn how to create a richer lifestyle which involves more freedom and a better well-being

Number of Pages Required

1 page

Font styles to use
Sans Serif
Other font styles liked:
• Roboto

Requirements
Should not have
• A cheezy unmodern landingpage with lots of texts and 10 sign-up buttons.
• This page is not a site about capturing emails and building lists by provide a "best-guide-for-something". It´s about getting people to book and pay for one or more coaching-sessions.

```html
<!DOCTYPE html>
<html lang="sv">
<head>
<meta charset="utf-8">
<title>Kelbro Studio – Coaching</title>
<link href="https://fonts.googleapis.com/css2?family=Open+Sans:ital,wght@0,400;0,600;0,700;0,800;1,400;1,600&display=swap" rel="stylesheet">
<style>
:root{
  --navy:#0f3f6b;
  --navy-deep:#0a2d50;
  --accent:#2aa3c9;
  --accent-dark:#1b7fa3;
  --sky:#a9dcea;
  --green:#2bb673;
  --ink:#333;
  --grey-box:#e6e8e8;
  --footer:#2a2a2a;
  --footer-deep:#1c1c1c;
  --bronze:#e08a3c;
  --silver:#a7a9ac;
  --gold:#e9a532;
}
*{box-sizing:border-box;margin:0;padding:0}
html,body{width:1200px;height:5187px;overflow:hidden}
body{font-family:"Open Sans",Arial,sans-serif;color:var(--ink);background:#fff;font-size:14px;line-height:1.6}
section,header,footer{position:relative;width:1200px;overflow:hidden}
.container{width:880px;margin:0 auto;position:relative}
.section-title{text-align:center;font-size:30px;font-weight:400;letter-spacing:1px;text-transform:uppercase;color:#222}
.section-title b{font-weight:800}
.btn-outline{display:inline-flex;align-items:center;gap:10px;border:2px solid var(--accent-dark);color:var(--accent-dark);font-size:12px;font-weight:700;letter-spacing:1px;padding:7px 16px;text-transform:uppercase}
.btn-outline .dot{width:20px;height:20px;border:2px solid currentColor;border-radius:50%;display:inline-flex;align-items:center;justify-content:center}

/* header */
.site-header{height:605px;background:linear-gradient(180deg,var(--navy-deep),var(--navy) 60%,#1d5f92)}
.header-bg{position:absolute;inset:80px 0 0 0;background:radial-gradient(ellipse at 50% 40%,rgba(70,140,200,.45),rgba(10,45,80,0) 70%)}
.brand{position:absolute;top:36px;left:0;right:0;display:flex;justify-content:center;align-items:center;gap:12px;color:#fff;font-size:26px;font-weight:700;letter-spacing:3px;text-transform:uppercase}
.brand .mark{width:22px;height:22px;background:var(--accent)}
.main-nav{position:absolute;top:110px;left:0;right:0;display:flex;justify-content:center;gap:26px}
.main-nav a{color:#fff;font-size:13px;font-weight:600;text-transform:uppercase;text-decoration:none}
.hero-photo{position:absolute;left:225px;top:172px;width:640px;height:433px;background:linear-gradient(180deg,rgba(40,90,140,0),rgba(30,60,90,.55))}

/* intro */
.intro{height:450px;background:var(--sky)}
.intro .section-title{padding-top:108px;color:var(--navy)}
.intro .section-title span{color:var(--accent-dark)}
.intro p{margin:40px auto 0;width:860px;text-align:center;font-size:13px;line-height:1.85;color:#2b4a5a}
.intro .cta{text-align:center;margin-top:40px}
.intro svg.edge{position:absolute;left:0;bottom:0}

/* matrix */
.matrix{height:615px}
.matrix .section-title{padding-top:60px}
.matrix-row{display:flex;gap:50px;margin-top:50px;align-items:flex-start}
.matrix-chart{width:400px;height:400px;flex:none;border-radius:8px;background:linear-gradient(135deg,#2f9fd8 0%,#f5a623 35%,#e4572e 65%,#3aa655 100%);opacity:.85}
.matrix-text{padding-top:70px;font-size:13px;color:#555;line-height:1.85}
.matrix-text .btn-outline{margin-top:24px;border-color:var(--green);color:var(--green)}

/* why */
.why{height:595px;background:linear-gradient(135deg,#3aa9c8,#7fc7dc 45%,#2f93b6)}
.why::before{content:"";position:absolute;inset:0;background:rgba(26,130,170,.35)}
.why .section-title{position:relative;padding-top:68px;color:#fff}
.why .section-title span{color:#0d4f74}
.why-grid{position:relative;display:flex;gap:28px;margin-top:70px;justify-content:center}
.why-card{width:200px;height:310px;background:rgba(255,255,255,.16);border:1px solid rgba(255,255,255,.5);text-align:center;padding:0 18px;position:relative}
.why-icon{width:110px;height:110px;border-radius:50%;background:#fff;margin:-30px auto 0;display:flex;align-items:center;justify-content:center;box-shadow:0 3px 8px rgba(0,0,0,.15)}
.why-card h3{margin-top:28px;font-size:19px;font-weight:400;color:#0d4560}
.why-card p{margin-top:14px;font-size:11.5px;line-height:1.75;color:#fff}

/* session */
.session{height:605px}
.session .section-title{padding-top:72px}
.session-grid{display:grid;grid-template-columns:420px 420px;gap:30px 26px;justify-content:center;margin-top:55px}
.session-item{background:var(--grey-box);height:160px;padding:22px 26px}
.session-item h4{font-size:15px;font-weight:600;color:#222;line-height:1.45}
.session-item p{margin-top:14px;font-size:11.5px;color:#666;line-height:1.7}

/* services */
.services{height:730px;background:radial-gradient(ellipse at 50% 35%,#6a6f78,#3a3e46 60%,#2c2f35)}
.services .section-title{padding-top:75px;color:#fff}
.services .lead{text-align:center;color:#fff;font-size:15px;margin-top:10px}
.products{display:flex;justify-content:center;gap:38px;margin-top:55px}
.product{width:270px;height:450px;position:relative}
.product-art{height:240px;border-radius:4px 4px 0 0}
.product.bronze .product-art{background:linear-gradient(160deg,#f2b36c,var(--bronze) 55%,#b8692b)}
.product.silver .product-art{background:linear-gradient(160deg,#d6d7d9,var(--silver) 55%,#7d7f83)}
.product.gold .product-art{background:linear-gradient(160deg,#f7d27a,var(--gold) 55%,#c07f1c)}
.product-body{background:#f6f6f6;height:210px;text-align:center;padding-top:22px;border-bottom:10px solid rgba(0,0,0,.12)}
.product-body h3{font-size:18px;font-weight:700;letter-spacing:1px;color:#222}
.product-body p{font-size:12.5px;color:#555;line-height:1.5;margin-top:4px}
.btn-order{display:inline-block;margin-top:22px;background:var(--green);color:#fff;font-size:13px;font-weight:700;padding:10px 24px;text-transform:uppercase;letter-spacing:.5px}

/* testimonials */
.testimonials{height:411px}
.testimonials .section-title{padding-top:70px}
.quotes{display:flex;gap:26px;justify-content:center;margin-top:62px}
.quote{width:420px;height:210px;background:var(--grey-box);text-align:center;padding:38px 30px 0;position:relative}
.quote-mark{position:absolute;top:-20px;left:50%;margin-left:-20px;width:40px;height:40px;border-radius:50%;background:var(--accent);display:flex;align-items:center;justify-content:center}
.quote blockquote{font-style:italic;font-size:13px;color:#444;line-height:1.7}
.quote cite{display:block;margin-top:14px;font-style:normal;font-weight:700;font-size:14px;color:#222}
.testimonials .rule{position:absolute;left:160px;right:160px;bottom:8px;height:2px;background:#e3e3e3}

/* coaches */
.coaches{height:606px;background:linear-gradient(180deg,#fff 0 440px,#eeeeee 440px)}
.coaches .section-title{padding-top:28px}
.coach-grid{display:flex;gap:52px;justify-content:center;margin-top:40px}
.coach{width:270px;height:500px;background:#fff;border:1px solid #dedede;text-align:center;position:relative}
.coach-tab{position:absolute;top:-1px;left:0;right:0;height:34px;background:var(--accent)}
.coach-tab span{position:absolute;left:50%;top:0;transform:translateX(-50%);background:#1b8fb8;color:#fff;font-size:12px;font-weight:700;padding:2px 20px}
.coach-head{margin-top:34px;padding-top:14px;height:82px;background:#e9eff1;font-size:22px;color:#555}
.coach-photo{width:120px;height:120px;border-radius:50%;margin:-28px auto 0;border:4px solid #fff;position:relative}
.coach h3{margin-top:18px;font-size:20px;font-weight:400;color:#222}
.coach .mail{font-size:12px;color:var(--accent)}
.coach p{margin:16px 30px 0;font-size:11.5px;line-height:1.7;color:#666}

/* connect */
.connect{height:224px;background:#eeeeee;text-align:center}
.connect h2{padding-top:128px;font-size:17px;font-weight:400;color:#999;letter-spacing:2px;text-transform:uppercase}
.social{display:flex;justify-content:center;gap:8px;margin-top:18px}
.social i{display:block;width:56px;height:56px;background:#3d5c7a}

/* footer */
.site-footer{height:346px;background:var(--footer)}
.footer-nav{display:flex;justify-content:center;gap:22px;padding-top:55px}
.footer-nav a{color:#ccc;font-size:12px;text-transform:uppercase;text-decoration:none}
.footer-brand{display:flex;justify-content:center;align-items:center;gap:10px;margin-top:28px;color:#fff;font-size:22px;font-weight:700;letter-spacing:3px;text-transform:uppercase}
.footer-brand .mark{width:18px;height:18px;background:var(--accent)}
.newsletter{display:flex;justify-content:center;align-items:center;gap:16px;margin-top:36px}
.newsletter label{color:#fff;font-weight:700;font-size:15px;text-transform:uppercase}
.newsletter .field{width:330px;height:34px;background:#fff;color:#999;font-size:12px;padding:8px 12px}
.newsletter .submit{height:34px;background:var(--accent);color:#fff;font-size:12px;font-weight:700;padding:8px 16px;text-transform:uppercase}
.contact{display:flex;justify-content:center;gap:60px;margin-top:30px;color:#bbb;font-size:12px}
.contact span{display:flex;align-items:center;gap:8px}
.contact svg{flex:none}
.copyright{position:absolute;left:0;right:0;bottom:0;height:52px;background:var(--footer-deep);color:#999;text-align:center;font-size:12px;line-height:52px}
</style>
</head>
<body>

<header class="site-header">
  <div class="header-bg" role="img" aria-label="Soft word cloud about coaching and lifestyle in blue tones"></div>
  <div class="brand"><span class="mark"></span>Kelbro Studio</div>
  <nav class="main-nav">
    <a href="#">Home</a><a href="#">About us</a><a href="#">Blog</a><a href="#">Coaching</a><a href="#">Testimonials</a><a href="#">Contact us</a>
  </nav>
  <div class="hero-photo" role="img" aria-label="Portrait photo of the two coaches standing together in suits"></div>
</header>

<section class="intro">
  <h2 class="section-title"><span>What</span> <b>we mean by a richer lifestyle</b></h2>
  <p>Lorem ipsum dolor sit amet, consectetur adipiscing elit, sed do eiusmod tempor incididunt ut labore et dolore magna aliqua. Ut enim ad minim veniam, quis nostrud exercitation ullamco laboris nisi ut aliquip ex ea commodo consequat. Duis aute irure dolor in reprehenderit in voluptate velit esse cillum dolore eu fugiat nulla pariatur. Excepteur sint occaecat cupidatat non proident, sunt in culpa qui officia deserunt mollit anim id est laborum.</p>
  <div class="cta"><span class="btn-outline">Read more <span class="dot"><svg width="8" height="8" viewBox="0 0 8 8"><path d="M2 1l4 3-4 3z" fill="currentColor"/></svg></span></span></div>
  <svg class="edge" width="1200" height="60" viewBox="0 0 1200 60"><polygon points="0,60 1200,0 1200,60" fill="#fff"/><polygon points="880,16 1200,0 1200,8 860,26" fill="#1b7fa3"/></svg>
</section>

<section class="matrix">
  <div class="container">
    <h2 class="section-title"><b>Our</b> Vardagskartan</h2>
    <div class="matrix-row">
      <div class="matrix-chart" role="img" aria-label="Vardagskartan illustration: a hand-lettered two by two lifestyle matrix in blue, orange, red and green with axis arrows"></div>
      <div class="matrix-text">
        <p>Lorem ipsum dolor sit amet, consectetur adipiscing elit, sed do eiusmod tempor incididunt ut labore et dolore magna aliqua. Ut enim ad minim veniam, quis nostrud exercitation ullamco laboris nisi ut aliquip ex ea commodo consequat. Duis aute irure dolor in reprehenderit in voluptate velit esse cillum dolore eu fugiat nulla pariatur. Excepteur sint occaecat cupidatat non proident, sunt in culpa qui officia deserunt mollit anim id est laborum.</p>
        <span class="btn-outline">Read more <span class="dot"><svg width="8" height="8" viewBox="0 0 8 8"><path d="M2 1l4 3-4 3z" fill="currentColor"/></svg></span></span>
      </div>
    </div>
  </div>
</section>

<section class="why" aria-label="Why choose coaching">
  <h2 class="section-title"><b>Why</b> <span>choose coaching</span></h2>
  <div class="why-grid">
    <div class="why-card">
      <div class="why-icon"><svg width="60" height="60" viewBox="0 0 60 60"><circle cx="30" cy="30" r="26" fill="#e4572e"/><circle cx="30" cy="30" r="18" fill="#fff"/><circle cx="30" cy="30" r="10" fill="#e4572e"/></svg></div>
      <h3>Targeting</h3>
      <p>Lorem ipsum dolor sit amet, consectetur adipiscing elit, sed do eiusmod tempor incididunt ut labore et dolore magna aliqua. Ut enim ad minim veniam.</p>
    </div>
    <div class="why-card">
      <div class="why-icon"><svg width="60" height="60" viewBox="0 0 60 60"><circle cx="30" cy="26" r="16" fill="#f5a623"/><rect x="23" y="40" width="14" height="10" rx="2" fill="#777"/></svg></div>
      <h3>Creating</h3>
      <p>Lorem ipsum dolor sit amet, consectetur adipiscing elit, sed do eiusmod tempor incididunt ut labore et dolore magna aliqua. Ut enim ad minim veniam.</p>
    </div>
    <div class="why-card">
      <div class="why-icon"><svg width="60" height="60" viewBox="0 0 60 60" fill="none" stroke-width="4"><path d="M10 50 L50 10" stroke="#3aa655"/><path d="M10 10 L50 50" stroke="#2f9fd8"/><circle cx="30" cy="30" r="5" fill="#e4572e" stroke="none"/></svg></div>
      <h3>Shaping</h3>
      <p>Lorem ipsum dolor sit amet, consectetur adipiscing elit, sed do eiusmod tempor incididunt ut labore et dolore magna aliqua. Ut enim ad minim veniam.</p>
    </div>
    <div class="why-card">
      <div class="why-icon"><svg width="60" height="60" viewBox="0 0 60 60"><circle cx="30" cy="30" r="24" fill="#1b5f8f"/><circle cx="30" cy="30" r="10" fill="#f5a623"/></svg></div>
      <h3>Capturing</h3>
      <p>Lorem ipsum dolor sit amet, consectetur adipiscing elit, sed do eiusmod tempor incididunt ut labore et dolore magna aliqua. Ut enim ad minim veniam.</p>
    </div>
  </div>
</section>

<section class="session">
  <h2 class="section-title"><b>What</b> happens during a typical coaching session</h2>
  <div class="session-grid">
    <div class="session-item"><h4>Lorem ipsum dolor sit amet, consectetur adipiscing elit.</h4><p>Sed ut perspiciatis unde omnis iste natus error sit voluptatem accusantium doloremque laudantium, totam rem aperiam, eaque ipsa quae ab illo inventore veritatis.</p></div>
    <div class="session-item"><h4>Lorem ipsum dolor sit amet, consectetur adipiscing elit.</h4><p>Sed ut perspiciatis unde omnis iste natus error sit voluptatem accusantium doloremque laudantium, totam rem aperiam, eaque ipsa quae ab illo inventore veritatis.</p></div>
    <div class="session-item"><h4>Lorem ipsum dolor sit amet, consectetur adipiscing elit.</h4><p>Sed ut perspiciatis unde omnis iste natus error sit voluptatem accusantium doloremque laudantium, totam rem aperiam, eaque ipsa quae ab illo inventore veritatis.</p></div>
    <div class="session-item"><h4>Lorem ipsum dolor sit amet, consectetur adipiscing elit.</h4><p>Sed ut perspiciatis unde omnis iste natus error sit voluptatem accusantium doloremque laudantium, totam rem aperiam, eaque ipsa quae ab illo inventore veritatis.</p></div>
  </div>
</section>

<section class="services">
  <h2 class="section-title"><b>What</b> services we provide</h2>
  <p class="lead">Choose product and click order</p>
  <div class="products">
    <div class="product bronze">
      <div class="product-art" role="img" aria-label="Bronze package box with bronze medal"></div>
      <div class="product-body"><h3>BRONZE</h3><p>Inkluderar 1 session<br>Pris 650 SEK</p><span class="btn-order">Order now</span></div>
    </div>
    <div class="product silver">
      <div class="product-art" role="img" aria-label="Silver package box with silver medal"></div>
      <div class="product-body"><h3>SILVER</h3><p>Inkluderar 5 sessioner<br>Pris 3050 SEK</p><span class="btn-order">Order now</span></div>
    </div>
    <div class="product gold">
      <div class="product-art" role="img" aria-label="Gold package box with gold medal"></div>
      <div class="product-body"><h3>GOLD</h3><p>Inkluderar 10 sessioner<br>Pris 5800 SEK</p><span class="btn-order">Order now</span></div>
    </div>
  </div>
</section>

<section class="testimonials">
  <h2 class="section-title">Testimonials</h2>
  <div class="quotes">
    <figure class="quote">
      <span class="quote-mark"><svg width="18" height="14" viewBox="0 0 18 14"><path d="M0 14V8C0 3 2 1 7 0v3C4 4 4 5 4 7h3v7zM11 14V8c0-5 2-7 7-8v3c-3 1-3 2-3 4h3v7z" fill="#fff"/></svg></span>
      <blockquote>”Uppiggande och inspirerande! Kommer med enkla vardagstips såväl som svårare tips. Ett roligt sätt att få en spark i baken, så att ekonomi-energin bibehålls! Tack för ett bra samtal!”</blockquote>
      <cite>- Annelie Brunstedt</cite>
    </figure>
    <figure class="quote">
      <span class="quote-mark"><svg width="18" height="14" viewBox="0 0 18 14"><path d="M0 14V8C0 3 2 1 7 0v3C4 4 4 5 4 7h3v7zM11 14V8c0-5 2-7 7-8v3c-3 1-3 2-3 4h3v7z" fill="#fff"/></svg></span>
      <blockquote>”Värdefullast för mig var kunskapen om alternativa investeringssställen som inte är börs eller eget ägande.”</blockquote>
      <cite>- Josefin Harkeby</cite>
    </figure>
  </div>
  <div class="rule"></div>
</section>

<section class="coaches">
  <h2 class="section-title"><b>About</b> the coaches</h2>
  <div class="coach-grid">
    <article class="coach">
      <div class="coach-tab"><span>HELLO</span></div>
      <div class="coach-head">My Name Is</div>
      <div class="coach-photo" role="img" aria-label="Portrait photo of coach Henrik Sandvall" style="background:linear-gradient(160deg,#8a7c70,#4a3e36)"></div>
      <h3>Henrik Sandvall</h3>
      <div class="mail">henrik@kelbrostudio.se</div>
      <p>Sed ut perspiciatis unde omnis iste natus error sit voluptatem accusantium doloremque laudantium, totam rem aperiam, eaque ipsa quae ab illo inventore veritatis.</p>
    </article>
    <article class="coach">
      <div class="coach-tab"><span>HELLO</span></div>
      <div class="coach-head">My Name Is</div>
      <div class="coach-photo" role="img" aria-label="Portrait photo of coach Oskar Lindmer" style="background:linear-gradient(160deg,#9fb07c,#5d6e48)"></div>
      <h3>Oskar Lindmer</h3>
      <div class="mail">oskar@kelbrostudio.se</div>
      <p>Sed ut perspiciatis unde omnis iste natus error sit voluptatem accusantium doloremque laudantium, totam rem aperiam, eaque ipsa quae ab illo inventore veritatis.</p>
    </article>
  </div>
</section>

<section class="connect">
  <h2>Connect with Kelbro Studio</h2>
  <div class="social"><i></i><i></i><i></i><i></i></div>
</section>

<footer class="site-footer">
  <nav class="footer-nav"><a href="#">Home</a><a href="#">About us</a><a href="#">Blog</a><a href="#">Coaching</a><a href="#">Testimonials</a><a href="#">Contact us</a></nav>
  <div class="footer-brand"><span class="mark"></span>Kelbro Studio</div>
  <div class="newsletter"><label>Sign up for our newsletter</label><span class="field">Enter your email address</span><span class="submit">Subscribe</span></div>
  <div class="contact">
    <span><svg width="14" height="14" viewBox="0 0 14 14"><circle cx="7" cy="7" r="6.5" fill="none" stroke="#bbb"/><path d="M7 3a2.5 2.5 0 0 1 2.5 2.5C9.5 7.5 7 11 7 11S4.5 7.5 4.5 5.5A2.5 2.5 0 0 1 7 3z" fill="#bbb"/></svg>Kelbro Studio AB, Ekgatan 12, 411 05 Göteborg</span>
    <span><svg width="14" height="14" viewBox="0 0 14 14"><circle cx="7" cy="7" r="6.5" fill="none" stroke="#bbb"/><path d="M4.5 4l1.5-.5 1 2-1 .8a5 5 0 0 0 1.7 1.7l.8-1 2 1-.5 1.5C7 10 4 7 4.5 4z" fill="#bbb"/></svg>031-555 01 20</span>
    <span><svg width="14" height="14" viewBox="0 0 14 14"><circle cx="7" cy="7" r="6.5" fill="none" stroke="#bbb"/><rect x="3.5" y="4.5" width="7" height="5" fill="none" stroke="#bbb"/><path d="M3.5 4.5 7 7.5l3.5-3" fill="none" stroke="#bbb"/></svg>info@kelbrostudio.se</span>
  </div>
  <div class="copyright">©2016 Kelbro Studio AB - All Rights Reserved</div>
</footer>

</body>
</html>
```